Update New Business Card - For Start Up

I need to update my business card, I have our old version for example. I would like to keep to the same colors and theme. We are a threat reporting and case management tool for corporations and educational institutions.

Target Market(s)

Corporate Security and Human Resources, School Administrators and Superintendents.

Industry/Entity Type

Physical Security and Technology.

Contact Information for Business Card

My Name, Founder/CEO, phone number 777-412-5068, Logo, Web...

Colors
0054AA
0677BA
7BADD7
CADEEF
E8F1F8

Requirements
Must have
• Something new and trendy.

```html
<!DOCTYPE html>
<html lang="en">
<head>
<meta charset="utf-8">
<title>Veltrace Business Card</title>
<link rel="stylesheet" href="https://fonts.googleapis.com/css2?family=Montserrat:wght@500;700&family=Poppins:wght@400&display=swap">
<style>
  :root {
    --backdrop: #d9dadc;
    --card-dark: #1c1d20;
    --brand-blue: #1c75bc;
    --text-grey: #c9cbcf;
    --title-grey: #a9acb2;
    --silver: #e8f1f8;
  }
  * { margin: 0; padding: 0; box-sizing: border-box; }
  html, body { width: 1200px; height: 800px; overflow: hidden; }
  body { background: var(--backdrop); position: relative; font-family: "Poppins", sans-serif; }

  .card {
    position: absolute;
    width: 540px;
    height: 310px;
    border-radius: 22px;
    box-shadow: 0 14px 30px rgba(0,0,0,0.25);
    overflow: hidden;
  }

  /* Front: contact side */
  .card-front { left: 80px; top: 80px; background: var(--card-dark); }
  .front-mark {
    position: absolute; left: 50px; top: 150px;
    width: 120px; height: 120px; border-radius: 50%;
    background: var(--brand-blue);
  }
  .identity { position: absolute; left: 215px; top: 58px; }
  .person-name {
    font-family: "Montserrat", sans-serif; font-weight: 700;
    font-size: 25px; letter-spacing: 0.5px; color: var(--brand-blue);
    text-transform: uppercase;
  }
  .person-title { font-size: 15px; color: var(--title-grey); margin-top: 2px; }
  .divider {
    position: absolute; left: 215px; right: 0; top: 136px;
    height: 2px; background: var(--brand-blue);
  }
  .contact-list { position: absolute; left: 215px; top: 156px; list-style: none; }
  .contact-item {
    display: flex; align-items: center; gap: 12px;
    font-size: 15px; color: var(--text-grey); line-height: 28px;
  }
  .contact-icon { width: 15px; height: 15px; flex: none; }

  /* Back: brand side */
  .card-back { left: 580px; top: 410px; background: var(--brand-blue); }
  .brand-lockup {
    position: absolute; inset: 0;
    display: flex; align-items: center; justify-content: center; gap: 20px;
  }
  .brand-dot { width: 64px; height: 64px; border-radius: 50%; background: var(--silver); }
  .brand-name {
    font-family: "Montserrat", sans-serif; font-weight: 500;
    font-size: 46px; letter-spacing: 8px; color: var(--silver);
    text-transform: uppercase;
  }
</style>
</head>
<body>
  <section class="card card-front">
    <div class="front-mark"></div>
    <div class="identity">
      <h1 class="person-name">Dana Korvath</h1>
      <p class="person-title">Founder/CEO</p>
    </div>
    <div class="divider"></div>
    <ul class="contact-list">
      <li class="contact-item">
        <svg class="contact-icon" viewBox="0 0 16 16" fill="none" stroke="#1c75bc" stroke-width="1.4"><path d="M3 1.5h3l1.2 3.2-1.8 1.2a8 8 0 0 0 4.7 4.7l1.2-1.8 3.2 1.2v3a1.5 1.5 0 0 1-1.5 1.5A12.5 12.5 0 0 1 1.5 3 1.5 1.5 0 0 1 3 1.5z"/></svg>
        <span>777-412-5068</span>
      </li>
      <li class="contact-item">
        <svg class="contact-icon" viewBox="0 0 16 16" fill="none" stroke="#1c75bc" stroke-width="1.4"><rect x="1" y="3" width="14" height="10" rx="1"/><path d="M1 3l7 6 7-6"/></svg>
        <span>dana@veltrace.co</span>
      </li>
      <li class="contact-item">
        <svg class="contact-icon" viewBox="0 0 16 16" fill="none" stroke="#1c75bc" stroke-width="1.4"><circle cx="8" cy="8" r="6.5"/><path d="M1.5 8h13M8 1.5c2 2 2 11 0 13M8 1.5c-2 2-2 11 0 13"/></svg>
        <span>veltrace.co</span>
      </li>
    </ul>
  </section>

  <section class="card card-back">
    <div class="brand-lockup">
      <div class="brand-dot"></div>
      <span class="brand-name">Veltrace</span>
    </div>
  </section>
</body>
</html>
```